Capability Statement Document/Flyer

Take the existing words from the capability statement document (attached) and design a unique folder/flyer document for professional use. Maybe something like a trifold or bifold style. Use approved colours and logo as per the attached files.
Our company designs and builds small onshore gas processing plants.

```html
<!DOCTYPE html>
<html lang="en">
<head>
<meta charset="utf-8">
<title>Streamwell Capability Statement 2026</title>
<link rel="stylesheet" href="https://fonts.googleapis.com/css2?family=Poppins:wght@400;500;600;700;800&display=swap">
<style>
:root{
  --teal:#1b7d6c;
  --teal-dark:#13665a;
  --teal-soft:#e3efec;
  --ink:#1f2a2b;
  --muted:#5d6a6b;
  --page:#ffffff;
  --page-grey:#eceeee;
  --canvas:#c4c6c6;
  --sky-top:#a9bccb;
  --sky-low:#d9dcd8;
  --ground:#8d8c84;
  --rule:#cfd6d5;
}
*{margin:0;padding:0;box-sizing:border-box}
html,body{width:1200px;height:800px;overflow:hidden}
body{background:var(--canvas);font-family:"Poppins",sans-serif;color:var(--ink);position:relative}
.page{position:absolute;top:200px;width:282px;height:399px;background:var(--page);overflow:hidden;box-shadow:0 6px 18px rgba(0,0,0,.18)}
.back-cover{left:24px}
.front-cover{left:306px}
.page-02{left:612px;background:var(--page-grey)}
.page-03{left:894px}

/* brand */
.brand{position:absolute;display:flex;align-items:center;gap:4px;font-weight:700;color:var(--teal);letter-spacing:.5px}
.brand-square{width:9px;height:9px;background:var(--teal)}

/* covers */
.cover-photo{position:absolute;left:0;right:0;bottom:0}
.front-cover .cover-photo{top:112px;background:linear-gradient(180deg,var(--sky-top) 0%,#c7d1d8 50%,var(--sky-low) 72%,var(--ground) 88%,#6f7770 100%)}
.back-cover .cover-photo{top:160px;background:linear-gradient(180deg,#b9c8d2 0%,#d3dad9 40%,#a9b5ad 62%,#4f8f80 80%,var(--teal) 100%)}
.title-box{position:absolute;background:var(--teal);color:#fff;padding:10px 12px}
.title-box h1{font-size:25px;line-height:.95;font-weight:800;letter-spacing:-.5px;text-transform:uppercase}
.title-box p{font-size:10px;line-height:1.25;margin-top:6px;font-weight:400}
.front-cover .title-box{left:28px;top:92px;width:200px}
.back-cover .title-box{left:20px;top:138px;width:200px}
.cover-url{position:absolute;font-size:7px;color:#fff}
.front-cover .cover-url{left:40px;top:206px}
.back-cover .cover-url{left:32px;top:252px}
.year{position:absolute;right:6px;font-size:74px;font-weight:700;line-height:1;color:rgba(190,196,200,.45);writing-mode:vertical-rl;transform:rotate(180deg);letter-spacing:-2px}
.front-cover .year{top:60px}
.back-cover .year{top:40px}
.cover-foot-url{position:absolute;right:14px;bottom:12px;font-size:6px;color:#fff}
.contact{position:absolute;left:20px;bottom:16px;color:#fff;font-size:6px;display:flex;gap:22px}
.contact h3{font-size:8px;font-weight:600;margin-bottom:4px}
.contact-line{display:flex;align-items:flex-start;gap:4px;margin-top:2px;line-height:1.3}
.contact-line svg{flex:none;margin-top:1px}

/* inner pages */
.running-head{position:absolute;left:18px;top:16px;display:flex;align-items:center;gap:5px;font-size:5px;color:var(--ink)}
.running-head b{font-size:6px;line-height:1;font-weight:700;text-transform:uppercase}
.running-head b span{color:var(--teal);display:block}
.running-head i{display:block;width:1px;height:12px;background:var(--ink)}
.page-02 h2{position:absolute;left:18px;top:40px;font-size:15px;font-weight:600}
.page-02 h2 span{color:var(--teal)}
.body-copy{position:absolute;left:18px;right:18px;font-size:5.2px;line-height:1.45;color:var(--ink)}
.tagline-bar{position:absolute;left:18px;width:200px;top:96px;background:var(--teal);color:#fff;font-size:7px;padding:3px 8px}
.sub-head{position:absolute;left:18px;font-size:8px;font-weight:600;color:var(--teal)}
.panel{position:absolute;left:0;right:0;top:154px;height:214px;background:var(--teal-soft)}
.principles{position:absolute;left:18px;top:170px;width:246px}
.principle{display:flex;height:14px;margin-top:3px}
.principle-num{width:14px;background:var(--teal-dark);color:#fff;font-size:6px;display:flex;align-items:center;justify-content:center}
.principle-text{flex:1;border:1px solid var(--teal);border-left:none;background:#fff;font-size:6px;color:var(--teal);display:flex;align-items:center;padding-left:6px}
.org{position:absolute;left:18px;top:236px;width:246px}
.org-row{display:flex;align-items:center;height:20px;margin-bottom:4px}
.org-label{width:70px;font-size:5px;font-weight:600;text-transform:uppercase;line-height:1.2}
.org-cells{flex:1;display:flex;gap:4px}
.org-cell{flex:1;height:16px;background:var(--teal);color:#fff;font-size:5.5px;display:flex;align-items:center;padding-left:6px}
.objective{position:absolute;left:18px;right:18px;top:320px;font-size:5.2px;line-height:1.45}
.objective b{display:block;color:var(--teal);font-size:7px;font-weight:600}
.foot-band{position:absolute;bottom:10px;height:12px;background:var(--teal);color:#fff;font-size:5px;display:flex;align-items:center;padding:0 8px;gap:6px}
.page-02 .foot-band{left:0;width:140px}
.page-03 .foot-band{right:0;width:150px;justify-content:flex-end}
.foot-url{position:absolute;bottom:13px;font-size:5px;color:var(--muted)}
.page-02 .foot-url{right:18px}
.page-03 .foot-url{left:18px}

/* services table */
.page-03 .brand{right:18px;top:18px;font-size:10px}
.services-title{position:absolute;left:18px;top:54px;font-size:8px;font-weight:600;color:var(--teal)}
.services{position:absolute;left:18px;right:18px;top:68px;border-collapse:collapse;font-size:5.4px;line-height:1.3}
.services th{background:var(--teal);color:#fff;font-weight:600;text-align:left;padding:4px 4px;font-size:6px}
.services td{border-bottom:1px solid var(--rule);padding:0 4px;height:22px;vertical-align:middle}
.services td.num{width:16px;text-align:center;color:var(--ink)}
.services td.fn{width:64px;color:var(--teal);font-weight:600}
</style>
</head>
<body>

<!-- Back cover -->
<section class="page back-cover">
  <div class="cover-photo" role="img" aria-label="Photo of an onshore gas processing plant with pipework under a pale sky, fading into teal"></div>
  <div class="year">2026</div>
  <div class="title-box">
    <h1>Capability<br>Statement</h1>
    <p>Simplify Project Execution,<br>Streamline Operations</p>
  </div>
  <div class="cover-url">www.streamwell.com.au</div>
  <div class="contact">
    <div>
      <h3>Contact Us</h3>
      <div class="contact-line">
        <svg width="6" height="7" viewBox="0 0 6 7"><path d="M3 0a2.5 2.5 0 0 0-2.5 2.5C.5 4.3 3 7 3 7s2.5-2.7 2.5-4.5A2.5 2.5 0 0 0 3 0zm0 3.4a.9.9 0 1 1 0-1.8.9.9 0 0 1 0 1.8z" fill="#e4d64a"/></svg>
        <span>12 Sample Rd<br>Perth WA 6000</span>
      </div>
    </div>
    <div style="padding-top:10px">
      <div class="contact-line">
        <svg width="6" height="6" viewBox="0 0 6 6"><circle cx="3" cy="3" r="3" fill="#e4d64a"/><path d="M2 1.5l.6.9-.4.4c.2.5.5.8 1 1l.4-.4.9.6-.4.6C2.9 4.4 1.6 3.1 1.4 2z" fill="#1b7d6c"/></svg>
        <span>+61 000 111 222</span>
      </div>
      <div class="contact-line">
        <svg width="6" height="6" viewBox="0 0 6 6"><rect x=".3" y="1.2" width="5.4" height="3.8" fill="#e4d64a"/><path d="M.3 1.2L3 3.3l2.7-2.1" stroke="#1b7d6c" stroke-width=".5" fill="none"/></svg>
        <span>info@streamwell.com.au</span>
      </div>
    </div>
  </div>
  <div class="cover-foot-url" style="bottom:70px">www.streamwell.com.au</div>
</section>

<!-- Front cover -->
<section class="page front-cover">
  <div class="brand" style="left:26px;top:38px;font-size:13px"><span class="brand-square"></span>STREAMWELL</div>
  <div class="cover-photo" role="img" aria-label="Photo of a gas processing facility with a shade canopy and pipework under a blue sky"></div>
  <div class="year">2026</div>
  <div class="title-box">
    <h1>Capability<br>Statement</h1>
    <p>Simplify Project Execution,<br>Streamline Operations</p>
  </div>
  <div class="cover-url">www.streamwell.com.au</div>
</section>

<!-- Page 02 -->
<section class="page page-02">
  <div class="running-head"><b>Capability<span>Statement</span></b><i></i>Simplify Project Execution, Streamline Operations</div>
  <h2>Who are <span>Streamwell?</span></h2>
  <p class="body-copy" style="top:64px">Streamwell are a highly experienced team of Executive, Project, Construction, Commissioning and Operations specialists who combine deep technical knowledge with proven leadership to deliver unique Project Delivery Partner services to organisations in Australia.</p>
  <div class="tagline-bar">Simplify Project Execution, Streamline Operations.</div>
  <div class="sub-head" style="top:114px">What is a Project Delivery Partner?</div>
  <p class="body-copy" style="top:126px">A Project Delivery Partner (PDP) provides integrated project management along with technical, commercial and delivery support services to help an organisation successfully deliver a project. The PDP acts as the owner's team while the owner retains accountability and key decision-making authority.</p>
  <div class="panel"></div>
  <div class="sub-head" style="top:160px">PDP Core Principles:</div>
  <div class="principles">
    <div class="principle"><span class="principle-num">1</span><span class="principle-text">Owner controls the project</span></div>
    <div class="principle"><span class="principle-num">2</span><span class="principle-text">PDP enables delivery &amp; provides assurance</span></div>
    <div class="principle"><span class="principle-num">3</span><span class="principle-text">Contractors execute the work</span></div>
  </div>
  <div class="org">
    <div class="org-row"><span class="org-label">Owner</span><div class="org-cells"><span class="org-cell">Operator XYZ</span></div></div>
    <div class="org-row"><span class="org-label">Project Delivery<br>Partner</span><div class="org-cells"><span class="org-cell">Streamwell</span></div></div>
    <div class="org-row"><span class="org-label">Contractors</span><div class="org-cells"><span class="org-cell">Engineering</span><span class="org-cell">Engineering</span><span class="org-cell">Execution</span></div></div>
  </div>
  <p class="objective"><b>PDP Objective:</b>Deliver the project safely, on schedule, within budget and ready for operations; providing owner capability throughout the project lifecycle.</p>
  <div class="foot-band"><span>02</span><span>Simplify Project Execution, Streamline Operations</span></div>
  <div class="foot-url">www.streamwell.com.au</div>
</section>

<!-- Page 03 -->
<section class="page page-03">
  <div class="brand"><span class="brand-square"></span>STREAMWELL</div>
  <div class="services-title">PDP Services:</div>
  <table class="services">
    <thead><tr><th>#</th><th>Function</th><th>Streamwell Service</th></tr></thead>
    <tbody>
      <tr><td class="num">1</td><td class="fn">Project Management</td><td>Planning, Reporting &amp; Delivery Leadership from Concept to Completion</td></tr>
      <tr><td class="num">2</td><td class="fn">Engineering</td><td>Concept Selection, Design Coordination, Technical Assurance &amp; Value Engineering</td></tr>
      <tr><td class="num">3</td><td class="fn">Procurement</td><td>Contracting Strategy, Tender Process &amp; Supplier/Contractor Management</td></tr>
      <tr><td class="num">4</td><td class="fn">Approvals</td><td>Land Access, Regulator Engagement, Safety Case, Permits &amp; Licenses</td></tr>
      <tr><td class="num">5</td><td class="fn">Cost Control</td><td>Budget Development, Forecasting &amp; Management</td></tr>
      <tr><td class="num">6</td><td class="fn">Scheduling</td><td>Master Schedule Development, WBS, Resource Allocation, Monitoring &amp; Updating</td></tr>
      <tr><td class="num">7</td><td class="fn">Risk Management</td><td>Risk Register, Identification, Mitigation &amp; Reporting</td></tr>
      <tr><td class="num">8</td><td class="fn">Governance</td><td>Framework, Stage Gates, Change control, Reporting &amp; Decision Support</td></tr>
      <tr><td class="num">9</td><td class="fn">Construction</td><td>Management &amp; Coordination of Contractor Execution Teams</td></tr>
      <tr><td class="num">10</td><td class="fn">Commissioning &amp; Start-up</td><td>Lead Commissioning &amp; Start-up, Completions System, Bring the Facility to Steady-State</td></tr>
      <tr><td class="num">11</td><td class="fn">Operations Readiness</td><td>People &amp; Organisation, Process &amp; Procedures, Systems &amp; Technology</td></tr>
      <tr><td class="num">12</td><td class="fn">Operations &amp; Maintenance</td><td>Monitor &amp; Operate Asset, Minimize Downtime, Lowest Possible OPEX for Owner</td></tr>
    </tbody>
  </table>
  <div class="foot-url">www.streamwell.com.au</div>
  <div class="foot-band"><span>Simplify Project Execution, Streamline Operations</span><span>03</span></div>
</section>

</body>
</html>
```